The hardcover "Star Chronicle" (large size, Quarto 4º, 12 × 9 1/2 in, 30.5 × 24.15 cm) in German language as follows:

STERNENCHRONIK (title)
der herausragendsten Unternehmer und Manager Deutschlands 2013 (subtitle 1)
BERLIN UND BRANDENBURG (subtitle 2, smaller than subtitle 1)

Morvalto (logo, WMF file attached)
Updates

Reason: The solutions are rather too childish and pre-made styles... is there anyone who can make it better? - a professional-looking business book (encyclopedia style, should have no color-pictures, no author's name, logo smaller due to the large size book)

Target Market(s)

business community

Requirements
Must have
• encyclopedia style large size book
must look professional and expensive

Nice to have
• - gold-color hardcover, or some gold-color elements
- some simple and decent graphic element (e.g. an ancient column, or some other architectural detail), if any
Should not have
• no color-pictures
no author's name

```html
<!DOCTYPE html>
<html lang="de">
<head>
<meta charset="utf-8">
<title>Sternenchronik – Buchumschlag</title>
<link rel="stylesheet" href="https://fonts.googleapis.com/css2?family=Cinzel:wght@400;700&family=Federo&display=swap">
<style>
  :root {
    --gold-top: #e4bd2e;
    --gold-mid: #e8d23e;
    --gold-bottom: #dcb228;
    --ink: #4b3b0e;
    --ink-soft: #5a4814;
    --emboss-light: rgba(255, 240, 150, 0.55);
    --emboss-dark: rgba(60, 40, 0, 0.45);
    --emblem-fill-top: #d9b22c;
    --emblem-fill-bottom: #cfa723;
    --emblem-edge: rgba(90, 65, 10, 0.55);
  }
  html, body {
    margin: 0;
    padding: 0;
    overflow: hidden;
    background: var(--gold-mid);
  }
  .cover {
    position: relative;
    width: 950px;
    height: 1200px;
    overflow: hidden;
    background: linear-gradient(180deg, var(--gold-top) 0%, var(--gold-mid) 50%, var(--gold-bottom) 100%);
  }
  .cover__grain {
    position: absolute;
    inset: 0;
    width: 950px;
    height: 1200px;
    opacity: 0.35;
    mix-blend-mode: multiply;
  }
  .cover__title {
    position: absolute;
    top: 138px;
    left: 0;
    width: 950px;
    margin: 0;
    text-align: center;
    font-family: "Federo", sans-serif;
    font-weight: 400;
    font-size: 60px;
    line-height: 72px;
    letter-spacing: 1px;
    color: var(--ink);
    text-shadow: 1px 1px 0 var(--emboss-light), -1px -1px 0 var(--emboss-dark);
  }
  .cover__subtitle {
    position: absolute;
    top: 238px;
    left: 0;
    width: 950px;
    margin: 0;
    text-align: center;
    font-family: "Cinzel", serif;
    font-weight: 700;
    font-size: 17.5px;
    line-height: 24px;
    letter-spacing: 0.2px;
    color: var(--ink-soft);
    text-shadow: 1px 1px 0 var(--emboss-light);
  }
  .cover__region {
    position: absolute;
    top: 287px;
    left: 0;
    width: 950px;
    margin: 0;
    text-align: center;
    font-family: "Cinzel", serif;
    font-weight: 700;
    font-size: 15.5px;
    line-height: 22px;
    letter-spacing: 0.4px;
    color: var(--ink-soft);
    text-shadow: 1px 1px 0 var(--emboss-light);
  }
  .cover__emblem {
    position: absolute;
    top: 368px;
    left: 406px;
    width: 144px;
    height: 178px;
    box-sizing: border-box;
    border-radius: 8px;
    border: 2px solid var(--emblem-edge);
    background: linear-gradient(180deg, var(--emblem-fill-top) 0%, var(--emblem-fill-bottom) 100%);
    box-shadow: inset 1px 1px 0 var(--emboss-light), 1px 1px 0 var(--emboss-light);
  }
  .cover__publisher {
    position: absolute;
    top: 1040px;
    left: 0;
    width: 950px;
    margin: 0;
    text-align: center;
    font-family: "Cinzel", serif;
    font-weight: 700;
    font-size: 64px;
    line-height: 80px;
    letter-spacing: 1px;
    color: var(--ink);
  }
</style>
</head>
<body>
  <main class="cover">
    <svg class="cover__grain" xmlns="http://www.w3.org/2000/svg" viewBox="0 0 950 1200" aria-hidden="true">
      <filter id="grain">
        <feTurbulence type="fractalNoise" baseFrequency="0.9" numOctaves="2" stitchTiles="stitch"/>
        <feColorMatrix type="matrix" values="0 0 0 0 0.55  0 0 0 0 0.42  0 0 0 0 0.05  0 0 0 1.2 -0.2"/>
      </filter>
      <rect width="950" height="1200" filter="url(#grain)"/>
    </svg>

    <h1 class="cover__title">STERNENCHRONIK</h1>
    <p class="cover__subtitle">der herausragendsten Unternehmer und Manager Deutschlands 2013</p>
    <p class="cover__region">Berlin und Brandenburg</p>

    <div class="cover__emblem" role="img" aria-label="Embossed line drawing of an Ionic column capital with three fluted shafts"></div>

    <p class="cover__publisher">Morvalto</p>
  </main>
</body>
</html>
```